Business Card for Yachting Management Company

Need a business card design for a new yachting project management company. Attached is the logo for the company.
Our clients are large yacht owners and captains.
Design must be in the style of the logo. Modern, elegant.

Example of data to show:
Peter Hollis
Project Manager
(+34) 612 738 104
peter@quorvane.net
Quorvane Management - Meridel Tower, Office 22 - KRB - Palma de Mallorca

The data above will have to be changed (by me) for the different people in the company over the next years.

Will be printed using PrintNova (Lustre Card Series). They provide these guidelines for the size:
"the actual size of the card is 1050 x 600 pixels. However, the full bleed size is 1083 x 633 pixels, and the safe printing area is 1008 x 558 pixels."

```html
<!DOCTYPE html>
<html lang="en">
<head>
<meta charset="utf-8">
<title>Quorvane Management – Business Card</title>
<link rel="stylesheet" href="https://fonts.googleapis.com/css2?family=Montserrat:wght@300;400;500;600;700&display=swap">
<style>
  :root {
    --backdrop: #2b2c2f;
    --silver-light: #dcdde0;
    --silver-mid: #c3c5c8;
    --silver-dark: #a7a9ad;
    --emboss: #f6f7f8;
    --engrave: #6a6d72;
    --line: #eef0f2;
    --line-soft: rgba(255,255,255,0.55);
  }
  * { margin: 0; padding: 0; box-sizing: border-box; }
  html, body {
    width: 1200px; height: 801px; overflow: hidden;
    background: var(--backdrop);
    font-family: "Montserrat", sans-serif;
  }
  .stage {
    position: relative; width: 1200px; height: 801px;
    display: flex; align-items: center; justify-content: center; gap: 28px;
  }
  .card { width: 560px; height: 320px; display: block; }
  .card text { font-family: "Montserrat", sans-serif; }
  .brand-name { fill: var(--engrave); font-weight: 600; }
  .brand-tag { fill: var(--engrave); font-weight: 500; }
  .brand-name--front, .brand-tag--front { fill: var(--emboss); }
  .person-first { fill: var(--emboss); font-weight: 700; }
  .person-last { fill: var(--emboss); font-weight: 300; }
  .person-role { fill: var(--emboss); font-weight: 400; }
  .contact-text { fill: var(--emboss); font-weight: 400; }
  .contact-phone { fill: var(--emboss); font-weight: 400; }
  .frame { fill: none; stroke: var(--line); stroke-width: 1.2; }
  .arc { fill: none; stroke: var(--line-soft); stroke-width: 1.4; }
  .icon { fill: none; stroke: var(--emboss); stroke-width: 1.2; stroke-linecap: round; stroke-linejoin: round; }
  .web-front { fill: var(--emboss); font-weight: 700; }
</style>
</head>
<body>
<main class="stage">

  <!-- Contact side -->
  <svg class="card card--contact" viewBox="0 0 560 320" aria-label="Business card, contact side">
    <defs>
      <linearGradient id="contactSurface" x1="0" y1="0" x2="1" y2="1">
        <stop offset="0" stop-color="#e2e3e5"/>
        <stop offset="0.6" stop-color="#cbcdd0"/>
        <stop offset="1" stop-color="#b6b8bb"/>
      </linearGradient>
      <clipPath id="contactClip"><rect width="560" height="320" rx="18"/></clipPath>
    </defs>
    <rect width="560" height="320" rx="18" fill="url(#contactSurface)"/>
    <g clip-path="url(#contactClip)">
      <circle class="arc" cx="-40" cy="170" r="248"/>
      <circle class="arc" cx="-40" cy="170" r="256"/>
    </g>

    <g class="brand">
      <rect x="30" y="146" width="10" height="10" fill="#6a6d72"/>
      <text class="brand-name" x="48" y="160" font-size="30">Quorvane</text>
      <text class="brand-tag" x="49" y="184" font-size="11" letter-spacing="5.5">MANAGEMENT</text>
    </g>

    <g class="person">
      <text x="262" y="52" font-size="22"><tspan class="person-first">PETER</tspan> <tspan class="person-last">HOLLIS</tspan></text>
      <text class="person-role" x="262" y="70" font-size="10">Project Manager</text>
    </g>

    <g class="contact-frames">
      <rect class="frame" x="292" y="84" width="248" height="28" rx="2"/>
      <rect class="frame" x="292" y="118" width="248" height="32" rx="2"/>
      <rect class="frame" x="292" y="156" width="248" height="22" rx="2"/>
      <rect class="frame" x="292" y="184" width="248" height="22" rx="2"/>
      <line class="frame" x1="292" y1="214" x2="540" y2="214"/>
    </g>

    <g class="contact-icons">
      <rect class="frame" x="262" y="122" width="22" height="22" rx="2"/>
      <path class="icon" d="M268 127 q-1 5 4 10 q5 5 9 4 l1-3 -3-2 -2 2 q-3-1-5-5 l2-2 -2-3z"/>
      <rect class="frame" x="262" y="150" width="22" height="22" rx="2"/>
      <circle class="icon" cx="273" cy="158" r="3"/>
      <path class="icon" d="M267 168 q6-8 12 0"/>
      <rect class="frame" x="262" y="178" width="22" height="22" rx="2"/>
      <rect class="icon" x="266" y="184" width="14" height="10"/>
      <path class="icon" d="M266 184 l7 6 7-6"/>
      <rect class="frame" x="262" y="206" width="22" height="22" rx="2"/>
      <circle class="icon" cx="273" cy="217" r="6"/>
      <path class="icon" d="M267 217 h12 M273 211 q-4 6 0 12 q4-6 0-12"/>
    </g>

    <g class="contact-details">
      <text class="contact-phone" x="302" y="105" font-size="19">(+34) 612 738 104</text>
      <text class="contact-text" x="302" y="131" font-size="8.5">Quorvane Management - Meridel Tower,</text>
      <text class="contact-text" x="302" y="144" font-size="8.5">Office 22 - KRB - Palma de Mallorca</text>
      <text class="contact-text" x="302" y="171" font-size="9">peter@quorvane.net</text>
      <text class="contact-text" x="302" y="199" font-size="9">www.quorvanemanagement.com</text>
    </g>
  </svg>

  <!-- Brand side -->
  <svg class="card card--brand" viewBox="0 0 560 320" aria-label="Business card, brand side">
    <defs>
      <linearGradient id="brandSurface" x1="0" y1="0" x2="1" y2="1">
        <stop offset="0" stop-color="#b1b3b6"/>
        <stop offset="0.55" stop-color="#c6c8cb"/>
        <stop offset="1" stop-color="#d7d8db"/>
      </linearGradient>
    </defs>
    <rect width="560" height="320" rx="18" fill="url(#brandSurface)"/>

    <line class="frame" x1="360" y1="62" x2="560" y2="62"/>

    <g class="brand brand--front">
      <rect x="108" y="88" width="20" height="20" fill="#f6f7f8"/>
      <text class="brand-name brand-name--front" x="140" y="128" font-size="58">Quorvane</text>
      <text class="brand-tag brand-tag--front" x="282" y="166" font-size="17" letter-spacing="9" text-anchor="middle">MANAGEMENT</text>
    </g>

    <rect class="frame" x="148" y="196" width="264" height="40" rx="14"/>
    <text class="web-front" x="280" y="221" font-size="14" text-anchor="middle">www.quorvanemanagement.com</text>

    <line class="frame" x1="0" y1="256" x2="560" y2="256"/>
    <line class="frame" x1="0" y1="264" x2="560" y2="264"/>
  </svg>

</main>
</body>
</html>
```